Bright Meadow Counseling Business Card design with a visually interesting use of Space

I need business cards that are luxurious and give a peaceful, calm vibe. I also had some letterhead designed, and i like the look of it also, it's attached with the logo design for reference/ ideas but feel free to be creative.

Target Market(s)

High end luxurious client who needs counseling

Industry/Entity Type

Marriage and Family Therapy

Contact Information for Business Card

Mira Kowalczyk MS LMFT/ or Toby Hallett address 4150 Larkin Suite 600

Font styles to use
Sans Serif

Colors
0054AA
0677BA
7BADD7
CADEEF
E8F1F8
0094D4
00A9DD
6FCCEA
C7EBF8
E9F6FB
A7469A
B969AE
D3A5CF
EDDBEB
F8F0F9
6B429C
8869AF
B7A5CE
E3DAEB
F3F0F8

Requirements
Must have
• Logo and color scheme but be simple modern and luxurious
Nice to have
• I'd like to incorporate some elelmets from the logo and letterhead into a simple modern card

```html
<!DOCTYPE html>
<html lang="en">
<head>
<meta charset="utf-8">
<title>Bright Meadow Counseling – Business Card</title>
<link href="https://fonts.googleapis.com/css2?family=Source+Sans+3:wght@300;400;700&display=swap" rel="stylesheet">
<style>
  :root {
    --backdrop: #d3d3d3;
    --card-white: #ffffff;
    --card-black: #050505;
    --brand-blue: #0054aa;
    --ink: #1d1d1d;
    --muted: #555555;
    --teal: #2bb3b1;
    --purple: #6b429c;
    --magenta: #a7469a;
    --sky: #0094d4;
    --wordmark: #e6e6e6;
  }
  * { box-sizing: border-box; margin: 0; padding: 0; }
  html, body {
    width: 1200px; height: 900px; overflow: hidden;
    background: var(--backdrop);
    font-family: "Source Sans 3", "Myriad Pro", Arial, sans-serif;
  }
  .canvas {
    position: relative; width: 1200px; height: 900px;
    display: flex; align-items: center; justify-content: center; gap: 60px;
  }
  .card { position: relative; width: 500px; height: 286px; }
  .card--front { background: var(--card-white); color: var(--ink); }
  .card--back { background: var(--card-black); }

  .holder { position: absolute; left: 40px; top: 46px; }
  .holder__name {
    color: var(--brand-blue); font-weight: 700; font-size: 21px;
    letter-spacing: 0.2px; text-transform: uppercase; line-height: 1;
  }
  .holder__title { font-size: 13px; color: var(--muted); margin-top: 4px; }

  .contact-list {
    position: absolute; left: 40px; top: 150px; list-style: none;
    font-size: 14px; line-height: 18px;
  }
  .contact-list li { display: flex; align-items: center; gap: 7px; }
  .contact-list svg { width: 12px; height: 12px; flex: none; }

  .brand-mark {
    position: absolute; right: 40px; top: 100px;
    display: flex; align-items: center; gap: 10px;
  }
  .brand-mark__dot { width: 34px; height: 34px; border-radius: 50%; background: var(--magenta); flex: none; }
  .brand-mark__name {
    font-weight: 300; font-size: 18px; color: var(--purple); line-height: 1.1; width: 120px;
  }

  .practice { position: absolute; right: 40px; bottom: 26px; text-align: right; font-size: 13px; line-height: 16px; }
  .practice__name { color: var(--brand-blue); }

  .wordmark {
    position: absolute; right: 70px; top: 80px;
    display: flex; flex-direction: column; align-items: flex-end; gap: 14px;
  }
  .wordmark__dot { width: 40px; height: 40px; border-radius: 50%; background: var(--magenta); margin-right: 40px; }
  .wordmark__name {
    color: var(--wordmark); font-weight: 300; font-size: 30px; line-height: 1.05;
    letter-spacing: 0.5px; text-align: right;
  }
</style>
</head>
<body>
<main class="canvas">
  <section class="card card--front" aria-label="Business card front">
    <div class="holder">
      <p class="holder__name">Mira Kowalczyk</p>
      <p class="holder__title">MS LMFT</p>
    </div>

    <div class="brand-mark">
      <span class="brand-mark__dot"></span>
      <span class="brand-mark__name">Bright Meadow Counseling</span>
    </div>

    <ul class="contact-list">
      <li>
        <svg viewBox="0 0 12 12"><path d="M2.5 1 L4.5 1 L5.2 3.5 L4 4.5 Q5 7 7.5 8 L8.5 6.8 L11 7.5 L11 9.5 Q11 11 9.5 11 Q1 10 1 2.5 Q1 1 2.5 1Z" fill="var(--sky)"/></svg>
        555-214-7730
      </li>
      <li>
        <svg viewBox="0 0 12 12"><rect x="3" y="1" width="6" height="3" fill="var(--purple)"/><rect x="1" y="4" width="10" height="5" rx="1" fill="var(--purple)"/><rect x="3" y="7" width="6" height="4" fill="#fff" stroke="var(--purple)"/></svg>
        555-214-7731
      </li>
      <li>
        <svg viewBox="0 0 12 12"><rect x="1" y="2.5" width="10" height="7" fill="var(--teal)"/><path d="M1 2.5 L6 7 L11 2.5" fill="none" stroke="#fff" stroke-width="1"/></svg>
        hello@brightmeadowcare.com
      </li>
      <li>
        <svg viewBox="0 0 12 12"><circle cx="6" cy="6" r="5" fill="var(--purple)"/><ellipse cx="6" cy="6" rx="2.2" ry="5" fill="none" stroke="#fff" stroke-width="0.8"/><path d="M1 6 H11 M2 3.5 H10 M2 8.5 H10" stroke="#fff" stroke-width="0.8"/></svg>
        www.brightmeadowcare.com
      </li>
    </ul>

    <div class="practice">
      <p class="practice__name">Bright Meadow Counseling</p>
      <p>4150 Larkin Suite 600, Cedar Vale, TX 75301</p>
    </div>
  </section>

  <section class="card card--back" aria-label="Business card back">
    <div class="wordmark">
      <span class="wordmark__dot"></span>
      <span class="wordmark__name">Bright Meadow<br>Counseling</span>
    </div>
  </section>
</main>
</body>
</html>
```